2022 American Football Calendar Design

This project is for an American High School Football calendar for 2022.

The theme is US football and specifically high-school football for a streaming TV show about American high-school football.

The total number of pages will be 28 with the cover being 4 pages and the months being the other 24 pages.

Design Elements:

1. Each month will have 2 pages. 1 for the lead / hero image and one for the days of the month.

2. We will supply the images for each month of the calendar. There may be multiple potential image options for a given month. You can, as the designer, choose to use one or multiple images for the month if you feel the design would benefit.

3. Each month will have special days including US Holidays and special Football Days. We will supply a spreadsheet with all of these days and dates.

4. The boxes for the days should be square with enough space to allow for writing in the box when the calendar is printed.

5. Each month will also have a special quote text area that will contain special informational or an inspirational quote.

6. The calendar dimensions are 11" x 8 1/2" (US Letter - landscape orientation) - folded. So each page is US Letter size. A print guide template is attached from the printing company.

7. The title of the calendar is Pinebrook Rally 2022 Calendar.

For this contest please supply design concepts for the following:
1. Cover page;
2. Inside page;
3. Month Hero page;
4. Days of the month page;
5. Back cover page;

We will use these design concepts to choose the winner who will then need to finish the complete calendar design and preparation for printing.

Final Deliverables:

A. Complete 28 page calendar design - the winner will complete the design and layout of all pages.

B. Final print ready PDF at least 350 dpi with bleed for printing. Please see the attached size template from the printing company with guides.

C. Layered & Fully Editable Source File - InDesign, AI or PSD (NO COREL DRAW PLEASE - Adobe products only please). If vector files are supplied, we will also need a text editable version.

D. Any fonts used - we have licensing, if needed, available from Quillon Type and Marvesta Assets.

We are looking for a fast turnaround on this project so it can be sent to the printer next week.

Target Market(s)

High-school football players and their family & friends

Industry/Entity Type

American football

Font styles to use
Other font styles liked:
• Collegiate type sports fonts.

Colors

Designer to choose colors to be used in the design.

Requirements
Must have
• 350 DPI print-ready PDF, Fully editable source files including fonts & layers (NO Corel Draw) - see brief
Nice to have
• vector (AI) and PSD
Should not have
• Do not use Corel Draw

```html
<!DOCTYPE html>
<html lang="en">
<head>
<meta charset="utf-8">
<title>Pinebrook Rally 2022 Calendar – Design Concepts</title>
<link href="https://fonts.googleapis.com/css2?family=Saira+Condensed:wght@500;700;800&family=Open+Sans:ital,wght@1,500&family=Special+Elite&display=swap" rel="stylesheet">
<style>
  :root{
    --canvas:#f4f4f2;
    --ink:#111111;
    --white:#ffffff;
    --gold:#f7c11c;
    --orange:#f28a1d;
    --magenta:#d6287a;
    --pink:#e6307c;
    --navy:#1d2a7a;
    --royal:#2a3fa3;
    --night:#191530;
    --olive:#8a8850;
    --olive-light:#d9d8bc;
    --slate:#3b3b3b;
    --slate-light:#cfcfcf;
    --rule:#c9c9c9;
  }
  *{box-sizing:border-box;margin:0;padding:0}
  html,body{width:1200px;height:791px;overflow:hidden;background:var(--canvas)}
  body{position:relative;font-family:"Saira Condensed",sans-serif;color:var(--ink)}

  .page{position:absolute;width:310px;height:240px;overflow:hidden;background:var(--white)}

  /* ---------- Front cover ---------- */
  .front-cover{left:55px;top:85px;background:linear-gradient(135deg,var(--gold) 0%,var(--orange) 45%,var(--magenta) 100%)}
  .front-cover .dark-field{position:absolute;left:18px;top:10px;width:300px;height:215px;background:var(--ink);border-radius:48% 0 52% 48% / 40% 0 60% 55%}
  .front-cover .hero-photo{position:absolute;left:-30px;top:70px;width:300px;height:155px;border-radius:50%;background:linear-gradient(180deg,#2a2626 0%,#3f4a3a 55%,#c4c4c4 85%,#5b5050 100%)}
  .cover-title{position:absolute;display:flex;align-items:flex-start;gap:4px;color:var(--white)}
  .cover-title .name{font-weight:700;font-size:12px;line-height:12px;text-align:right;padding-top:6px;text-transform:uppercase}
  .cover-title .year-block{display:flex;flex-direction:column}
  .cover-title .year{font-weight:800;font-size:46px;line-height:36px;background:linear-gradient(180deg,var(--gold),var(--orange) 70%,var(--magenta));-webkit-background-clip:text;background-clip:text;color:transparent}
  .cover-title .word{font-family:"Special Elite",monospace;font-size:11px;letter-spacing:5px;line-height:14px}
  .front-cover .cover-title{right:16px;top:14px}
  .studio-mark{position:absolute;display:flex;align-items:center;gap:4px;font-weight:700;font-size:9px;letter-spacing:.5px;text-transform:uppercase}
  .studio-mark .dot{width:7px;height:7px;border-radius:50%;background:currentColor}
  .front-cover .studio-mark{right:12px;bottom:10px;color:var(--navy)}

  /* ---------- Back cover ---------- */
  .back-cover{left:30px;top:385px;background:var(--night)}
  .back-cover .hero-photo{position:absolute;left:120px;top:-10px;width:230px;height:225px;border-radius:55% 0 0 55% / 50% 0 0 50%;background:radial-gradient(ellipse at 60% 40%,#5a1c1c 0%,#2a0f12 55%,#140a14 100%)}
  .back-cover .swoosh{position:absolute;left:0;bottom:0;width:310px;height:80px}
  .back-cover .studio-mark{left:54px;top:62px;color:var(--white)}
  .back-cover .cover-title{left:14px;top:80px}

  /* ---------- Month hero pages ---------- */
  .hero-page{background:linear-gradient(160deg,var(--accent-light),var(--accent) 90%)}
  .hero-page .hero-photo{position:absolute;left:-10px;top:8px;width:320px;height:226px;border-radius:50%}
  .jan{--accent:var(--olive);--accent-light:var(--olive-light)}
  .feb{--accent:var(--slate);--accent-light:var(--slate-light)}
  .hero-jan{left:500px;top:20px}
  .hero-jan .hero-photo{background:linear-gradient(180deg,#2f3a34 0%,#566645 45%,#7f8a52 100%)}
  .hero-feb{left:850px;top:305px}
  .hero-feb .hero-photo{background:linear-gradient(180deg,#7a7873 0%,#5f5a52 50%,#8a7a60 100%)}

  /* ---------- Days of the month pages ---------- */
  .cal-jan{left:500px;top:260px}
  .cal-feb{left:850px;top:545px}
  .cal-page .backdrop{position:absolute;inset:0;width:310px;height:240px}
  .year-tag{position:absolute;left:6px;top:32px;width:92px;height:20px;background:var(--accent);color:var(--white);font-weight:700;font-size:17px;line-height:20px;padding-left:14px;clip-path:polygon(0 0,82% 0,100% 100%,0 100%)}
  .month-title{position:absolute;right:10px;top:12px;display:flex;align-items:center;gap:4px;color:var(--accent);font-weight:800;font-size:24px;line-height:24px;text-transform:uppercase}
  .month-title .month-num{background:var(--accent);color:var(--white);font-size:17px;line-height:20px;padding:0 5px;clip-path:polygon(12% 0,100% 0,100% 100%,0 100%)}
  .quote{position:absolute;left:6px;top:92px;width:64px;font-family:"Open Sans",sans-serif;font-style:italic;font-size:7.5px;line-height:14px;text-align:center;color:var(--ink)}
  .quote::before,.quote::after{display:block;font-family:Georgia,serif;font-style:normal;font-weight:700;font-size:16px;line-height:10px;color:var(--accent)}
  .quote::before{content:"\201C";text-align:left}
  .quote::after{content:"\201D";text-align:right;padding-top:4px}
  .days{position:absolute;left:76px;top:52px;width:226px;border-collapse:collapse;table-layout:fixed;background:var(--white)}
  .days th{height:15px;font-weight:700;font-size:9px;border:1px solid var(--rule);color:var(--ink)}
  .days th.sun{background:var(--pink);color:var(--white)}
  .days td{height:25px;border:1px solid var(--rule);text-align:center;font-weight:700;font-size:12px}
  .days td.sun{color:var(--pink);background:linear-gradient(90deg,#fbe0ea,var(--white))}
  .fine-print{position:absolute;left:8px;bottom:5px;font-family:"Open Sans",sans-serif;font-size:4px;color:#555}

  /* ---------- Yearly planner ---------- */
  .planner{left:390px;top:515px}
  .planner .backdrop{position:absolute;inset:0;width:310px;height:240px}
  .planner-title{position:absolute;left:0;right:0;top:14px;display:flex;justify-content:center;align-items:center;gap:3px}
  .planner-title .year{font-weight:800;font-size:30px;line-height:28px;background:linear-gradient(90deg,var(--navy) 50%,var(--pink) 50%);-webkit-background-clip:text;background-clip:text;color:transparent}
  .planner-title .label{font-weight:800;font-size:11px;line-height:10px;text-transform:uppercase;color:var(--navy)}
  .planner-title .label span{display:block;color:var(--pink)}
  .month-grid{position:absolute;left:12px;top:52px;width:286px;display:grid;grid-template-columns:repeat(4,1fr);gap:4px}
  .month-box{height:56px;border:1px solid #9aa0c8;background:repeating-linear-gradient(180deg,transparent 0 7px,#c6c9dc 7px 8px) 0 10px/100% 46px no-repeat,var(--white)}
  .month-box h3{font-weight:700;font-size:6px;text-align:center;line-height:9px;text-transform:uppercase;color:var(--pink)}
  .month-box.q1 h3{color:var(--olive)}
  .month-box.q1.dark h3{color:var(--slate)}
</style>
</head>
<body>

<!-- Front cover -->
<section class="page front-cover">
  <div class="dark-field"></div>
  <div class="hero-photo" role="img" aria-label="Night game photo of high-school football players running downfield"></div>
  <div class="cover-title">
    <div class="name">Pinebrook<br>Rally</div>
    <div class="year-block"><span class="year">2022</span><span class="word">CALENDAR</span></div>
  </div>
  <div class="studio-mark"><span class="dot"></span>Lakeshore Tales Media</div>
</section>

<!-- Back cover -->
<section class="page back-cover">
  <div class="hero-photo" role="img" aria-label="Dark red-lit photo of a player holding up a football helmet"></div>
  <svg class="swoosh" viewBox="0 0 310 80" aria-hidden="true">
    <path d="M0 40 C90 80 200 75 310 30 L310 80 L0 80 Z" fill="#2a3fa3"/>
    <path d="M0 58 C100 90 220 80 310 52 L310 80 L0 80 Z" fill="#3b2f8f"/>
  </svg>
  <div class="studio-mark"><span class="dot"></span>Lakeshore Tales Media</div>
  <div class="cover-title">
    <div class="name">Pinebrook<br>Rally</div>
    <div class="year-block"><span class="year">2022</span><span class="word">CALENDAR</span></div>
  </div>
</section>

<!-- January hero -->
<section class="page hero-page hero-jan jan">
  <div class="hero-photo" role="img" aria-label="Photo of a young athlete reaching for a pass on a practice field"></div>
</section>

<!-- January days -->
<section class="page cal-page cal-jan jan">
  <svg class="backdrop" viewBox="0 0 310 240" aria-hidden="true">
    <path d="M0 0 H310 V40 C220 0 100 0 0 40 Z" fill="#d9d8bc"/>
    <path d="M0 200 C90 250 230 240 310 200 V240 H0 Z" fill="#b9b78a"/>
    <path d="M0 215 C110 250 230 245 310 222 V240 H0 Z" fill="#8a8850"/>
  </svg>
  <div class="year-tag">2022</div>
  <div class="month-title">January <span class="month-num">01</span></div>
  <p class="quote">Don't wait for opportunity, Create it</p>
  <table class="days">
    <tr><th class="sun">SUN</th><th>MON</th><th>TUE</th><th>WED</th><th>THU</th><th>FRI</th><th>SAT</th></tr>
    <tr><td class="sun"></td><td></td><td></td><td></td><td></td><td></td><td>1</td></tr>
    <tr><td class="sun">2</td><td>3</td><td>4</td><td>5</td><td>6</td><td>7</td><td>8</td></tr>
    <tr><td class="sun">9</td><td>10</td><td>11</td><td>12</td><td>13</td><td>14</td><td>15</td></tr>
    <tr><td class="sun">16</td><td>17</td><td>18</td><td>19</td><td>20</td><td>21</td><td>22</td></tr>
    <tr><td class="sun">23</td><td>24</td><td>25</td><td>26</td><td>27</td><td>28</td><td>29</td></tr>
    <tr><td class="sun">30</td><td>31</td><td></td><td></td><td></td><td></td><td></td></tr>
  </table>
  <p class="fine-print">*Dates and game days subject to change by league schedule</p>
</section>

<!-- Yearly planner -->
<section class="page planner">
  <svg class="backdrop" viewBox="0 0 310 240" aria-hidden="true">
    <path d="M0 0 H310 V40 C220 -5 90 -5 0 60 Z" fill="#9aa3d0"/>
    <path d="M0 0 H120 C60 10 20 30 0 60 Z" fill="#2a3fa3"/>
    <path d="M0 180 C80 250 230 245 310 190 V240 H0 Z" fill="#9aa3d0"/>
    <path d="M0 205 C100 255 240 245 310 215 V240 H0 Z" fill="#1d2a7a"/>
  </svg>
  <div class="planner-title">
    <span class="year">2022</span>
    <span class="label">Yearly<span>Planner</span></span>
  </div>
  <div class="month-grid">
    <div class="month-box q1"><h3>January</h3></div>
    <div class="month-box q1 dark"><h3>February</h3></div>
    <div class="month-box"><h3>March</h3></div>
    <div class="month-box"><h3>April</h3></div>
    <div class="month-box"><h3>May</h3></div>
    <div class="month-box"><h3>June</h3></div>
    <div class="month-box"><h3>July</h3></div>
    <div class="month-box"><h3>August</h3></div>
    <div class="month-box"><h3>September</h3></div>
    <div class="month-box"><h3>October</h3></div>
    <div class="month-box"><h3>November</h3></div>
    <div class="month-box"><h3>December</h3></div>
  </div>
</section>

<!-- February hero -->
<section class="page hero-page hero-feb feb">
  <div class="hero-photo" role="img" aria-label="Photo of a young archer drawing a compound bow beside his coach"></div>
</section>

<!-- February days -->
<section class="page cal-page cal-feb feb">
  <svg class="backdrop" viewBox="0 0 310 240" aria-hidden="true">
    <path d="M0 0 H310 V40 C220 0 100 0 0 40 Z" fill="#e2e2e2"/>
    <path d="M0 200 C90 250 230 240 310 200 V240 H0 Z" fill="#bdbdbd"/>
    <path d="M0 215 C110 250 230 245 310 222 V240 H0 Z" fill="#6d6d6d"/>
  </svg>
  <div class="year-tag">2022</div>
  <div class="month-title">February <span class="month-num">02</span></div>
  <p class="quote">Don't wait for opportunity, Create it</p>
  <table class="days">
    <tr><th class="sun">SUN</th><th>MON</th><th>TUE</th><th>WED</th><th>THU</th><th>FRI</th><th>SAT</th></tr>
    <tr><td class="sun"></td><td></td><td>1</td><td>2</td><td>3</td><td>4</td><td>5</td></tr>
    <tr><td class="sun">6</td><td>7</td><td>8</td><td>9</td><td>10</td><td>11</td><td>12</td></tr>
    <tr><td class="sun">13</td><td>14</td><td>15</td><td>16</td><td>17</td><td>18</td><td>19</td></tr>
    <tr><td class="sun">20</td><td>21</td><td>22</td><td>23</td><td>24</td><td>25</td><td>26</td></tr>
    <tr><td class="sun">27</td><td>28</td><td></td><td></td><td></td><td></td><td></td></tr>
    <tr><td class="sun"></td><td></td><td></td><td></td><td></td><td></td><td></td></tr>
  </table>
  <p class="fine-print">*Dates and game days subject to change by league schedule</p>
</section>

</body>
</html>
```